Nutrition Infographic for weight loss- key points and nutrition habits for after weight loss surgery

I need someone to put together some infographics based on some nutrition information I have put together. We are a company who do weight loss surgery for patients and I am trying to put together some resources for patients so they can look after their nutrition for the long term.

I have some info and ideas on how we can execute this on paper but I need some a creative genius with top notch design skills to help me put it together.

I am basically after two infographics- One with the nutrition information I have outlined and One with the pyramid I have illustrated. Please let me know if you need clarification on the layout. Also happy to take on board any ideas you might have too!

If more time is needed with adjustments/refinements I understand and am happy to work with you to get to a final product we are happy with.

Target Market(s)

weight loss clients- ages ranging mostly from 20-45 male and female.

Industry/Entity Type

Health Care

Colors

Designer to choose colors to be used in the design.

Requirements
Must have
• Simple, clean concepts and images are needed.
• Easy to understand layout to enhance uptake of understanding the information

```html
<!DOCTYPE html>
<html lang="en">
<head>
<meta charset="utf-8">
<title>Good Nutrition Habits for Life</title>
<link rel="stylesheet" href="https://fonts.googleapis.com/css2?family=Fredoka:wght@600&family=Oswald:wght@500&family=Open+Sans:wght@600;700&display=swap">
<style>
  :root {
    --mint-bg: #aae8da;
    --panel: #5fcfba;
    --panel-dark: #52c4ae;
    --orange: #f7941d;
    --white: #ffffff;
    --ink: #2f3b3a;
    --ribbon: #ffffff;
  }
  * { box-sizing: border-box; margin: 0; padding: 0; }
  html, body { width: 1200px; height: 2294px; overflow: hidden; }
  body {
    background: var(--mint-bg);
    font-family: "Open Sans", Arial, sans-serif;
    position: relative;
  }
  .frame {
    position: absolute; inset: 0;
    border: 6px solid var(--orange);
    pointer-events: none;
  }
  .title-ribbon {
    position: absolute; left: 100px; top: 18px; width: 1000px; height: 96px;
  }
  .title-ribbon h1 {
    position: absolute; inset: 0;
    display: flex; align-items: center; justify-content: center;
    font-family: "Fredoka", sans-serif; font-weight: 600;
    font-size: 66px; color: var(--orange); letter-spacing: 0.5px;
  }
  .panel {
    position: absolute; left: 40px;
    background: var(--panel);
    border-radius: 10px 28px 10px 22px;
    box-shadow: inset 0 -4px 0 var(--panel-dark);
  }
  .note {
    color: var(--white); font-weight: 600; font-size: 25px; line-height: 1.33;
    padding: 20px 30px 20px 18px;
  }
  .note p + p { margin-top: 24px; }
  .intro p { padding-left: 12px; }
  .section-label {
    position: absolute; top: 0; bottom: 0;
    display: flex; align-items: center; justify-content: center; text-align: center;
    font-family: "Oswald", sans-serif; font-weight: 500;
    font-size: 29px; line-height: 1.22; color: var(--white); text-transform: uppercase;
    white-space: nowrap;
  }
  .item {
    position: absolute; transform: translateX(-50%);
    display: flex; flex-direction: column; align-items: center;
  }
  .art {
    width: 112px; height: 112px; border-radius: 50%;
    border: 5px solid rgba(255,255,255,0.85);
    background: var(--tone);
  }
  .art.wide { width: 215px; border-radius: 56px; }
  .item-name {
    margin-top: 2px;
    font-size: 19px; font-weight: 600; color: var(--ink); white-space: nowrap;
  }
</style>
</head>
<body>
  <div class="frame"></div>

  <header class="title-ribbon">
    <svg width="1000" height="96" viewBox="0 0 1000 96" aria-hidden="true">
      <polygon points="0,8 1000,8 960,48 1000,88 0,88 40,48" fill="var(--ribbon)"/>
    </svg>
    <h1>Good Nutrition Habits for Life</h1>
  </header>

  <section class="panel intro" style="top:136px;width:1086px;height:296px;">
    <div class="note">
      <p>You have taken steps to lose weight and look after your health so we can take this opportunity to create some good nutrition habits for now and for the long term.</p>
      <p>You will learn to focus on food for nourishing your body with the right balance to keep you satisfied and to fuel yourself for journey ahead.</p>
      <p>To make things easier we are going to breakdown different food groups and prioritise them based on how much your body needs them.</p>
    </div>
  </section>

  <section class="panel" style="top:474px;width:1086px;height:122px;">
    <div class="note">
      <p>EVERYDAY FOODS- Include these on a regular basis as they are generally whole foods, less processed and high in nutrient quality. There is no substitute for the naturally occurring vitamins, minerals and anti-oxidants which we find in food.</p>
    </div>
  </section>

  <section class="panel" style="top:627px;width:1115px;height:161px;">
    <h2 class="section-label" style="left:0;width:250px;">High Quality<br>Proteins</h2>
  </section>
  <div class="item" style="left:370px;top:636px"><div class="art" style="--tone:radial-gradient(#d98a45,#a85a25)" role="img" aria-label="Roast chicken illustration"></div><span class="item-name">Chicken</span></div>
  <div class="item" style="left:508px;top:636px"><div class="art" style="--tone:radial-gradient(#d2434a,#9c2630)" role="img" aria-label="Steak illustration"></div><span class="item-name">Meat</span></div>
  <div class="item" style="left:647px;top:636px"><div class="art" style="--tone:radial-gradient(#e0707a,#5aa8d8)" role="img" aria-label="Mince on a plate illustration"></div><span class="item-name">Mince</span></div>
  <div class="item" style="left:788px;top:636px"><div class="art" style="--tone:radial-gradient(#f48a5c,#e2633a)" role="img" aria-label="Salmon fillet illustration"></div><span class="item-name">Fish</span></div>
  <div class="item" style="left:930px;top:636px"><div class="art" style="--tone:radial-gradient(#f09a5a,#3f7fc0)" role="img" aria-label="Seafood platter illustration"></div><span class="item-name">Seafood</span></div>
  <div class="item" style="left:1065px;top:636px"><div class="art" style="--tone:radial-gradient(#ffc23a,#f4f4f4 45%,#5aa8d8)" role="img" aria-label="Fried eggs illustration"></div><span class="item-name">Eggs</span></div>

  <section class="panel" style="top:817px;width:708px;height:161px;">
    <h2 class="section-label" style="left:0;width:240px;">Dairy</h2>
  </section>
  <div class="item" style="left:370px;top:813px"><div class="art" style="--tone:radial-gradient(#ffffff,#5aa8d8)" role="img" aria-label="Milk bottle and glass illustration"></div><span class="item-name">Milk</span></div>
  <div class="item" style="left:508px;top:813px"><div class="art" style="--tone:radial-gradient(#ffcf4a,#f0a52a 60%,#5aa8d8)" role="img" aria-label="Cheese wedge illustration"></div><span class="item-name">Chesse</span></div>
  <div class="item" style="left:647px;top:813px"><div class="art" style="--tone:radial-gradient(#ffffff,#f07f3a 70%,#5aa8d8)" role="img" aria-label="Yoghurt cups illustration"></div><span class="item-name">Yoghurt</span></div>

  <section class="panel" style="top:1005px;width:853px;height:153px;">
    <h2 class="section-label" style="left:0;width:240px;">Fresh Fruit<br>and Vegetables</h2>
  </section>
  <div class="item" style="left:450px;top:1014px"><div class="art wide" style="--tone:linear-gradient(90deg,#e8443a,#7ab83a,#ffc82a,#f7941d)" role="img" aria-label="Assorted fresh fruit illustration"></div><span class="item-name">Fresh Fruits</span></div>
  <div class="item" style="left:732px;top:1014px"><div class="art wide" style="--tone:linear-gradient(90deg,#d84545,#f07a2a,#6a3b7a,#5fb63a,#ffc82a)" role="img" aria-label="Assorted vegetables illustration"></div><span class="item-name">Vegetables</span></div>

  <section class="panel" style="top:1187px;width:1131px;height:156px;">
    <h2 class="section-label" style="left:0;width:240px;">Wholegrains,<br>Quality Carbs</h2>
  </section>
  <div class="item" style="left:388px;top:1192px"><div class="art" style="--tone:radial-gradient(#c9843f,#8a5426)" role="img" aria-label="Multigrain bread illustration"></div><span class="item-name">Multigrain Bread</span></div>
  <div class="item" style="left:557px;top:1192px"><div class="art" style="--tone:radial-gradient(#8a6a55,#6e8fa8)" role="img" aria-label="Bowl of brown rice illustration"></div><span class="item-name">Brown rice</span></div>
  <div class="item" style="left:692px;top:1192px"><div class="art" style="--tone:radial-gradient(#d6a866,#b07e3e)" role="img" aria-label="Rolled oats illustration"></div><span class="item-name">Rolled oats</span></div>
  <div class="item" style="left:857px;top:1192px"><div class="art" style="--tone:radial-gradient(#e0504a,#b42a2a)" role="img" aria-label="Sweet potato illustration"></div><span class="item-name">Sweet potato</span></div>
  <div class="item" style="left:985px;top:1192px"><div class="art" style="--tone:radial-gradient(#a87a55,#5a3e2a)" role="img" aria-label="Quinoa illustration"></div><span class="item-name">Quinoa</span></div>

  <section class="panel" style="top:1367px;width:491px;height:169px;">
    <h2 class="section-label" style="left:6px;width:230px;">Legumes, Pulses,<br>Nuts, Seeds</h2>
  </section>
  <div class="item" style="left:420px;top:1384px"><div class="art wide" style="--tone:linear-gradient(90deg,#8a2a2a,#c98a4a,#6a4a2a,#e8c87a,#2a2a2a)" role="img" aria-label="Beans, nuts and seeds illustration"></div></div>

  <section class="panel" style="top:1367px;left:571px;width:600px;height:169px;">
    <h2 class="section-label" style="left:0;width:150px;">Hydration</h2>
  </section>
  <div class="item" style="left:812px;top:1383px"><div class="art" style="--tone:radial-gradient(#dff3ff,#5ab0e0)" role="img" aria-label="Water bottle and glass illustration"></div><span class="item-name">Water</span></div>
  <div class="item" style="left:941px;top:1383px"><div class="art" style="--tone:radial-gradient(#f4eedc,#c9a86a)" role="img" aria-label="Cup of tea illustration"></div><span class="item-name">Tea</span></div>
  <div class="item" style="left:1070px;top:1383px"><div class="art" style="--tone:radial-gradient(#6a3e1e,#f4f4f4 70%)" role="img" aria-label="Cup of coffee illustration"></div><span class="item-name">Coffee</span></div>

  <section class="panel" style="top:1567px;width:1086px;height:122px;">
    <div class="note">
      <p>SOMETIMES FOODS- These might have been a big part of your diet before you decided to take steps to improve your health and lose weight. Long term success does require some sacrifices and consistency so we will not include these items often.</p>
    </div>
  </section>

  <section class="panel" style="top:1718px;width:1115px;height:156px;">
    <h2 class="section-label" style="left:0;width:200px;">Sweets</h2>
  </section>
  <div class="item" style="left:370px;top:1726px"><div class="art" style="--tone:radial-gradient(#6a3a22,#3e2012)" role="img" aria-label="Chocolate pieces illustration"></div><span class="item-name">Chocolates</span></div>
  <div class="item" style="left:508px;top:1726px"><div class="art" style="--tone:radial-gradient(#ffffff,#f06aa8)" role="img" aria-label="Lollipop illustration"></div><span class="item-name">Lollies</span></div>
  <div class="item" style="left:647px;top:1726px"><div class="art" style="--tone:radial-gradient(#f0a0c0,#d9a060)" role="img" aria-label="Ice cream cone illustration"></div><span class="item-name">Ice Cream</span></div>
  <div class="item" style="left:788px;top:1726px"><div class="art" style="--tone:linear-gradient(#e8443a,#ffc82a,#5fb63a)" role="img" aria-label="Ice block illustration"></div><span class="item-name">Ice Blocks</span></div>
  <div class="item" style="left:936px;top:1726px"><div class="art" style="--tone:radial-gradient(#f0b44a,#c9843f)" role="img" aria-label="Biscuits illustration"></div><span class="item-name">Biscuits</span></div>
  <div class="item" style="left:1065px;top:1726px"><div class="art" style="--tone:linear-gradient(#5a2e1a,#d9a56a,#5a2e1a)" role="img" aria-label="Slice of chocolate cake illustration"></div><span class="item-name">Cakes</span></div>

  <section class="panel" style="top:1906px;width:1131px;height:161px;">
    <h2 class="section-label" style="left:0;width:200px;">High Sugar<br>Drinks</h2>
  </section>
  <div class="item" style="left:370px;top:1910px"><div class="art" style="--tone:radial-gradient(#ffffff,#d8262e 60%)" role="img" aria-label="Soft drink can illustration"></div><span class="item-name">Soft drinks</span></div>
  <div class="item" style="left:512px;top:1910px"><div class="art" style="--tone:radial-gradient(#ffb43a,#f07f1a)" role="img" aria-label="Glass of orange juice illustration"></div><span class="item-name">fruit juice</span></div>
  <div class="item" style="left:676px;top:1910px"><div class="art" style="--tone:radial-gradient(#b6e05a,#7ab83a)" role="img" aria-label="Iced tea cup illustration"></div><span class="item-name">Sweet iced teas</span></div>
  <div class="item" style="left:855px;top:1910px"><div class="art" style="--tone:radial-gradient(#c8d8e8,#2a6ab0)" role="img" aria-label="Energy drink can illustration"></div><span class="item-name">Energy drinks</span></div>
  <div class="item" style="left:1012px;top:1910px"><div class="art" style="--tone:radial-gradient(#e8f4ff,#3a8ad0)" role="img" aria-label="Sports drink bottle illustration"></div><span class="item-name">Sports drinks</span></div>

  <section class="panel" style="top:2099px;width:936px;height:161px;">
    <h2 class="section-label" style="left:4px;width:270px;">High Fat Content,<br>Poor Quality Foods</h2>
  </section>
  <div class="item" style="left:402px;top:2108px"><div class="art" style="--tone:radial-gradient(#c9843f,#8a5426)" role="img" aria-label="Pastry pie illustration"></div><span class="item-name">Pastries</span></div>
  <div class="item" style="left:555px;top:2108px"><div class="art" style="--tone:linear-gradient(#f0a040,#5fb63a,#e8443a,#7a3e1e,#f0a040)" role="img" aria-label="Burger illustration"></div><span class="item-name">Fast Food</span></div>
  <div class="item" style="left:695px;top:2108px"><div class="art" style="--tone:radial-gradient(#ffd86a,#4a90c8)" role="img" aria-label="Bowl of crisps illustration"></div><span class="item-name">Crisps</span></div>
  <div class="item" style="left:849px;top:2108px"><div class="art" style="--tone:radial-gradient(#d98a45,#f4f4f4 75%)" role="img" aria-label="Fried chicken bucket illustration"></div><span class="item-name">Fried Foods</span></div>
</body>
</html>
```